Twin Curtain Evening - Split Poster Design

We are an amateur theatre group based in Geneva, Switzerland. We take pride in eye-catching posters for our shows, which are printed in various sizes.
Unfortunately our budget is limited so we are not able to pay more than $10 for any stock images or art that is used on the posters. Please keep this in mind when searching for appropriate images.
This design will be for two original one-act comedies which will perform in late April 2016. Proceeds will go to charity. We would like a split design in a vertical poster format. It is up to you whether this is a horizontal or diagonal split, but there should be a clear division between the two.
Here are plot summaries for the two plays. To be clear, the plot summaries and the publicity texts SHOULD NOT APPEAR ON THE POSTER.
Play 1, The Quarterly Tryst
A man attending a business meeting with a client in a hotel discovers the "client" is his ex-fiancée and accidentally locks himself in a closet in an attempt to hide from her. They end up hashing out the details of their failed relationship through the closet door, and end by reconciling.
Here is the text we are using to publicize it:
The Quarterly Tryst is a comedy that sets out to push the envelope on business communications while simultaneously moving forward within an end-user perspective of Anglo-French relations. The drama unfolds against a background of delicious international cuisine. A parody of management-speak, you’ll be rooting for the characters in a not-so-classic story of unrequited love.
Here are some design suggestions, but very open to other ideas:
A background of a hotel bedroom. It's a very simple set - basically a bed and a closet. Maybe an image of the closet with a sign on the door - for example "Service Only".
Play 2, Counter Lass
Plot summary: Maeve takes a part-time job at a recently-opened "adult store" in her small village in Ireland. There is the humor of small-town folk being confronted with the sex shop, as well as the more serious backdrop of Maeve learning that the owner of the shop was the former lover of her father.
Publicity text:
In Counter Lass, Maeve, a college student struggling to pay her way during the economic crisis in Ireland, decides to take an unusual part-time job. Can a small community in “Holy Catholic Ireland” find its way out of the dark ages and into the 21st century? Counter Lass is a comedy with a serious, relevant and contemporary message.
Design suggestions (open to other ideas): photographic style, vivid or deep colours, lots of shade.
Here is the information that needs to be on the poster, wherever you see fit:
Play 1:
play title: The Quarterly Tryst
author byline: by Rex Dunmore
Play 2:
play title: Counter Lass
author byline: by Aoibheann Kustner
Applies to both:
No need to include the words before the colons, they are just for clarity:
date: 29-30 April 2016
time: 20:00 (or 8pm, up to designer)
location:
École de Gestion Lucien-Ferrand
rue des Pâquerettes 14
Geneva
websites:
www.vmtk.ch
www.stagewordsnorth.ch
The poster should say "Twin Curtain Evening"
"Proceeds to charity"
Attached you will find a template for our posters. This simply has our group name and logo in the top right corner: (Lakeside Anglophone Stage Circle presents).
You may change the color of both the text and the logo, but please do not change the font, size, or location.
Technical Details:
Any font or combination of fonts is acceptable. The largest text should be the play titles.
For this competition, we would like the version with A3 proportions, which will also be used at A5 size (14.8 x 21 cm). Therefore no text should be below 9pt at A5.
However, from the winning designer we will also need repurposed sizes of the same design. Here is a comprehensive list of the sizes we will need.
1) A3 print poster. Artwork should be 300dpi, CMYK, sent with a 1mm bleed all round, to specification PDF/X-1A:2001. We will need this image in PDF format in addition to the default Pixelfair formats.
2) Horizontal A6 JPG. This will be used as an advertisement in another play's programme. The text will have to be resized. If the original poster is vertical, then other changes will have to be made, of course.
2) Chatterly advert picture. 1200px by 628px, RGB jpeg. This must comply with Chatterly’s restrictions on amount of text, which is no more than 20% of area taken up by text.(https://www.chatterly-example.net/ads/tools/text_overlay).
Because of these restrictions it is sufficient to include just the title and the author's name in this version.
3) Chatterly cover picture: 851px by 314px. RGB jpeg. It is sufficient to include just the title and the author's name in this version.
4) Web banner. 1000px by 300px. RGB jpeg. This version should include just the main image(s), no text.
5) Square version. Main images, no text. 600px x 600px
6) For a very particular website: 1280px x 960px

```html
<!DOCTYPE html>
<html lang="en">
<head>
<meta charset="utf-8">
<title>Twin Curtain Evening</title>
<link rel="stylesheet" href="https://fonts.googleapis.com/css2?family=Oswald:wght@400;600;700&family=Montserrat:wght@400;600;700&family=Dancing+Script:wght@700&display=swap">
<style>
  :root {
    --tan: #c9a566;
    --ink: #2a2016;
    --cream: #fbf3e2;
    --suit-dark: #1b1b1d;
    --suit-mid: #3a3a3e;
    --pink-light: #f6c9cf;
    --pink: #e9a3ae;
    --red: #c8232c;
    --white: #ffffff;
  }
  html, body { margin: 0; padding: 0; overflow: hidden; }
  body { width: 849px; height: 1200px; background: var(--tan); }
  .poster {
    position: relative; width: 849px; height: 1200px; overflow: hidden;
    background: var(--tan);
    font-family: "Montserrat", Arial, sans-serif; color: var(--ink);
  }
  .evening-title {
    position: absolute; left: 28px; top: 18px; margin: 0;
    font-family: "Oswald", "Arial Narrow", sans-serif; font-weight: 700; font-style: italic;
    font-size: 32px; letter-spacing: 0.5px; line-height: 1; color: var(--ink);
  }
  .charity {
    position: absolute; left: 150px; top: 56px; margin: 0;
    font-family: "Oswald", "Arial Narrow", sans-serif; font-weight: 600; font-style: italic;
    font-size: 15px; letter-spacing: 1px; color: var(--ink);
  }
  .presenter {
    position: absolute; right: 112px; top: 14px; text-align: right;
    font-family: "Montserrat", Arial, sans-serif; font-weight: 700;
    font-size: 16px; line-height: 1.2; color: var(--white);
  }
  .presenter-mark {
    position: absolute; right: 24px; top: 12px; width: 78px; height: 78px;
    border-radius: 50%; background: var(--white);
  }
  .frame { position: absolute; left: 56px; width: 737px; }
  .frame svg { position: absolute; inset: 0; }
  .frame-one { top: 150px; height: 460px; }
  .frame-two { top: 622px; height: 460px; }
  .scene {
    position: absolute; left: 26px; right: 26px; top: 24px; bottom: 24px; overflow: hidden;
  }
  .scene-business { background: linear-gradient(90deg, var(--suit-mid) 0%, var(--suit-dark) 45%, #141416 100%); }
  .scene-business .photo {
    position: absolute; left: 0; top: 0; bottom: 0; width: 52%;
    background: linear-gradient(100deg, #e7e1da 0%, #5a5a60 40%, var(--suit-dark) 100%);
  }
  .scene-counter { background: linear-gradient(90deg, var(--pink-light) 0%, var(--pink) 100%); }
  .scene-counter .photo {
    position: absolute; right: 0; top: 0; bottom: 0; width: 48%;
    background: radial-gradient(ellipse at 60% 45%, #f2d3c8 0%, #e9b0b6 55%, rgba(233,163,174,0) 80%);
  }
  .play-title {
    position: absolute; margin: 0;
    font-family: "Oswald", "Arial Narrow", sans-serif; font-weight: 700;
    text-transform: uppercase; line-height: 0.98; color: var(--white);
  }
  .title-business { left: 380px; top: 66px; font-size: 56px; }
  .byline {
    position: absolute; margin: 0; font-family: "Montserrat", Arial, sans-serif;
    font-size: 14px; font-style: italic; color: var(--white);
  }
  .byline-business { left: 384px; top: 336px; }
  .title-counter { left: 36px; top: 150px; font-size: 60px; letter-spacing: 1px; }
  .title-counter .script {
    display: block; font-family: "Dancing Script", cursive; text-transform: none;
    color: var(--red); font-size: 64px; margin-left: 150px; margin-top: -8px;
  }
  .byline-counter { left: 200px; top: 298px; color: var(--red); }
  .date {
    position: absolute; right: 28px; top: 1090px; margin: 0;
    font-family: "Oswald", "Arial Narrow", sans-serif; font-weight: 700;
    font-size: 40px; line-height: 1; color: var(--cream); letter-spacing: 0.5px;
  }
  .venue {
    position: absolute; right: 28px; top: 1142px; margin: 0; text-align: right;
    font-family: "Oswald", "Arial Narrow", sans-serif; font-weight: 600;
    font-size: 15px; letter-spacing: 0.3px; color: var(--ink); line-height: 1.4;
  }
</style>
</head>
<body>
<main class="poster">
  <h1 class="evening-title">TWIN CURTAIN EVENING</h1>
  <p class="charity">PROCEEDS TO CHARITY</p>

  <div class="presenter">Lakeside Anglophone<br>Stage Circle<br>presents</div>
  <div class="presenter-mark"></div>

  <section class="frame frame-one">
    <svg width="737" height="460" viewBox="0 0 737 460">
      <path d="M20 4 H717 A16 16 0 0 0 733 20 V440 A16 16 0 0 0 717 456 H20 A16 16 0 0 0 4 440 V20 A16 16 0 0 0 20 4 Z" fill="var(--tan)" stroke="var(--ink)" stroke-width="2"/>
      <rect x="18" y="16" width="701" height="428" fill="none" stroke="var(--cream)" stroke-width="2"/>
    </svg>
    <div class="scene scene-business">
      <div class="photo" role="img" aria-label="Photograph of a man in a dark suit and white shirt, a woman's hand with red nails pulling his tie"></div>
      <h2 class="play-title title-business">The<br>Quarterly<br>Tryst</h2>
      <p class="byline byline-business">by Rex Dunmore</p>
    </div>
  </section>

  <section class="frame frame-two">
    <svg width="737" height="460" viewBox="0 0 737 460">
      <path d="M20 4 H717 A16 16 0 0 0 733 20 V440 A16 16 0 0 0 717 456 H20 A16 16 0 0 0 4 440 V20 A16 16 0 0 0 20 4 Z" fill="var(--tan)" stroke="var(--ink)" stroke-width="2"/>
      <rect x="18" y="16" width="701" height="428" fill="none" stroke="var(--cream)" stroke-width="2"/>
    </svg>
    <div class="scene scene-counter">
      <div class="photo" role="img" aria-label="Photograph of a red-haired young woman covered in pink sticky notes on a pink background"></div>
      <h2 class="play-title title-counter">Counter<span class="script">lass</span></h2>
      <p class="byline byline-counter">by Aoibheann Kustner</p>
    </div>
  </section>

  <p class="date">29-30 APRIL 2016 AT 8PM</p>
  <p class="venue">ÉCOLE DE GESTION LUCIEN-FERRAND RUE DES PÂQUERETTES 14, GENEVA<br>www.vmtk.ch &nbsp;|&nbsp; www.stagewordsnorth.ch</p>
</main>
</body>
</html>
```